Business card and stationary
Business card and stationary for medical office
Bright & Fun-filled
Gregory L. Hollis, MD
2846 Orwen Ln, Suite B
Lindale, TX 75829
hcplindale@mailpost.example
www.korvafamilypractice.example
logo images uploaded - please feel free to crop out the main logo. Also, on the card somewhere needs the statement, "a KOFP Clinic"
Appointment card and logo
Master logo - I eould encourage you to use the circle logo in creative and unique ways. Please add the tagline, "a KOFP clinic" under the "Hollis Care Partners"

```html
<!DOCTYPE html>
<html lang="en">
<head>
<meta charset="utf-8">
<title>Hollis Care Partners – Stationery</title>
<link href="https://fonts.googleapis.com/css2?family=Open+Sans:wght@400;600&display=swap" rel="stylesheet">
<style>
  :root {
    --brand-blue: #234f9b;
    --brand-blue-dark: #1a3c78;
    --rule-grey: #c9ccd3;
    --paper: #ffffff;
    --board-light: #bdbdbd;
    --board-dark: #8c8c8c;
    --ink: #3a3f4a;
    --caption: #e8e8e8;
  }
  * { box-sizing: border-box; margin: 0; padding: 0; }
  html, body { width: 1200px; height: 725px; overflow: hidden; }
  body {
    position: relative;
    font-family: "Open Sans", Arial, sans-serif;
    background: radial-gradient(ellipse at 50% 40%, var(--board-light), var(--board-dark));
  }
  .piece {
    position: absolute;
    background: var(--paper);
    box-shadow: 0 2px 5px rgba(0,0,0,.35);
    overflow: hidden;
  }
  .piece.blue { background: var(--brand-blue); }
  .wave { position: absolute; left: 0; top: 0; width: 100%; height: 100%; }
  .caption {
    position: absolute;
    font-size: 5px;
    color: var(--caption);
    text-align: center;
    white-space: nowrap;
  }
  .brand {
    position: absolute;
    display: flex;
    align-items: center;
    gap: .35em;
    color: var(--brand-blue);
    font-weight: 600;
    line-height: 1.05;
  }
  .brand.on-blue { color: var(--paper); }
  .brand-dot {
    width: 1.6em; height: 1.6em;
    border-radius: 50%;
    background: currentColor;
    flex: none;
  }
  .brand-name { display: flex; flex-direction: column; }
  .brand-tag { font-weight: 600; font-size: .55em; letter-spacing: .05em; }
  .contact {
    position: absolute;
    font-size: 4px;
    line-height: 1.45;
    color: var(--ink);
  }
  .contact.on-blue { color: var(--paper); }
  .appt-line { display: block; border-bottom: 1px solid var(--rule-grey); margin-top: 7px; width: 70px; }
  .appt-title { font-size: 5px; font-weight: 600; color: var(--brand-blue); }
  .on-blue .appt-title { color: var(--paper); }
  .on-blue .appt-line { border-color: rgba(255,255,255,.5); }
  .envelope-back { position: absolute; background: var(--paper); box-shadow: 0 2px 5px rgba(0,0,0,.35); overflow: hidden; }
</style>
</head>
<body>

<!-- Business card front -->
<div class="piece" style="left:60px;top:53px;width:168px;height:96px">
  <svg class="wave" viewBox="0 0 100 100" preserveAspectRatio="none">
    <path d="M0 68 C35 52 65 92 100 62 L100 100 L0 100Z" fill="var(--rule-grey)"/>
    <path d="M0 74 C35 58 65 98 100 68 L100 100 L0 100Z" fill="var(--brand-blue)"/>
  </svg>
  <div class="brand" style="left:8px;top:9px;font-size:7px"><span class="brand-dot"></span><span class="brand-name">Hollis Care Partners<span class="brand-tag">a KOFP clinic</span></span></div>
  <div class="contact" style="left:8px;top:50px">Gregory L. Hollis, MD</div>
</div>
<div class="caption" style="left:60px;top:152px;width:168px">Business Card Front</div>

<!-- Business card back -->
<div class="piece blue" style="left:252px;top:53px;width:168px;height:96px">
  <svg class="wave" viewBox="0 0 100 100" preserveAspectRatio="none">
    <path d="M0 70 C35 56 65 96 100 66 L100 100 L0 100Z" fill="var(--paper)"/>
  </svg>
  <div class="contact on-blue" style="left:78px;top:10px">2846 Orwen Ln, Suite B<br>Lindale, TX 75829<br>hcplindale@mailpost.example<br>www.korvafamilypractice.example</div>
</div>
<div class="caption" style="left:252px;top:152px;width:168px">Business Card Back</div>

<!-- Small card front -->
<div class="piece" style="left:432px;top:53px;width:108px;height:79px">
  <svg class="wave" viewBox="0 0 100 100" preserveAspectRatio="none">
    <path d="M0 58 C35 44 65 80 100 50 L100 100 L0 100Z" fill="var(--brand-blue)"/>
  </svg>
  <div class="brand" style="left:7px;top:8px;font-size:5px"><span class="brand-dot"></span><span class="brand-name">Hollis Care Partners<span class="brand-tag">a KOFP clinic</span></span></div>
</div>
<div class="caption" style="left:432px;top:135px;width:108px">Small Card Front</div>

<!-- Appointment card front -->
<div class="piece" style="left:60px;top:211px;width:168px;height:89px">
  <div class="brand" style="left:8px;top:8px;font-size:6px"><span class="brand-dot"></span><span class="brand-name">Hollis Care Partners<span class="brand-tag">a KOFP clinic</span></span></div>
  <div class="contact" style="left:60px;top:30px"><span class="appt-title">Your Next Appointment</span><span class="appt-line"></span><span class="appt-line"></span></div>
</div>
<div class="caption" style="left:60px;top:303px;width:168px">Appointment Card Front</div>

<!-- Appointment card back -->
<div class="piece blue" style="left:252px;top:211px;width:168px;height:89px">
  <div class="contact on-blue" style="left:50px;top:26px"><span class="appt-title">Your Next Appointment</span><span class="appt-line"></span><span class="appt-line"></span></div>
</div>
<div class="caption" style="left:252px;top:303px;width:168px">Appointment Card Back</div>

<!-- Small card back -->
<div class="piece blue" style="left:432px;top:228px;width:108px;height:72px">
  <svg class="wave" viewBox="0 0 100 100" preserveAspectRatio="none">
    <path d="M0 72 C35 58 65 94 100 64 L100 100 L0 100Z" fill="var(--paper)"/>
  </svg>
</div>
<div class="caption" style="left:432px;top:303px;width:108px">Small Card Back</div>

<!-- Envelope front -->
<div class="piece" style="left:612px;top:163px;width:192px;height:89px">
  <svg class="wave" viewBox="0 0 100 100" preserveAspectRatio="none">
    <path d="M0 62 C35 50 65 88 100 58 L100 100 L0 100Z" fill="var(--rule-grey)"/>
    <path d="M0 68 C35 56 65 94 100 64 L100 100 L0 100Z" fill="var(--brand-blue)"/>
  </svg>
  <div class="brand" style="left:7px;top:7px;font-size:5px"><span class="brand-dot"></span><span class="brand-name">Hollis Care Partners<span class="brand-tag">a KOFP clinic</span></span></div>
  <div class="contact on-blue" style="left:140px;top:70px;font-size:3.5px">2846 Orwen Ln, Suite B<br>Lindale, TX 75829</div>
</div>
<div class="caption" style="left:612px;top:255px;width:192px">Envelope Front</div>

<!-- Envelope backs -->
<div class="envelope-back" style="left:828px;top:96px;width:300px;height:60px">
  <svg class="wave" viewBox="0 0 100 100" preserveAspectRatio="none">
    <rect width="100" height="100" fill="#2a2a2a"/>
    <path d="M0 0 L50 80 L100 0Z" fill="#111"/>
  </svg>
</div>
<div class="envelope-back" style="left:828px;top:130px;width:300px;height:70px">
  <svg class="wave" viewBox="0 0 100 100" preserveAspectRatio="none">
    <path d="M0 0 L100 0 L100 45 C70 65 30 30 0 55Z" fill="var(--brand-blue)"/>
  </svg>
</div>
<div class="envelope-back" style="left:828px;top:180px;width:300px;height:84px">
  <svg class="wave" viewBox="0 0 100 100" preserveAspectRatio="none">
    <path d="M0 0 L100 0 L100 40 C70 60 30 25 0 50Z" fill="var(--brand-blue)"/>
  </svg>
</div>
<div class="caption" style="left:828px;top:267px;width:300px">Envelope Back</div>

<!-- Letterhead 1 -->
<div class="piece" style="left:60px;top:336px;width:264px;height:348px">
  <svg class="wave" viewBox="0 0 100 100" preserveAspectRatio="none">
    <path d="M0 84 C35 77 65 95 100 80 L100 100 L0 100Z" fill="var(--rule-grey)"/>
    <path d="M0 86 C35 79 65 97 100 82 L100 100 L0 100Z" fill="var(--brand-blue)"/>
  </svg>
  <div class="brand" style="left:12px;top:14px;font-size:9px"><span class="brand-dot"></span><span class="brand-name">Hollis Care Partners<span class="brand-tag">a KOFP clinic</span></span></div>
  <div class="contact on-blue" style="left:195px;top:318px">2846 Orwen Ln, Suite B<br>Lindale, TX 75829</div>
</div>
<div class="caption" style="left:60px;top:687px;width:264px">Letterhead Option 1</div>

<!-- Letterhead 2 -->
<div class="piece" style="left:372px;top:336px;width:264px;height:348px">
  <svg class="wave" viewBox="0 0 100 100" preserveAspectRatio="none">
    <path d="M0 86 C35 78 65 96 100 82 L100 100 L0 100Z" fill="var(--brand-blue)"/>
    <path d="M0 88 C35 80 65 98 100 84 L100 100 L0 100Z" fill="#8d8f94"/>
  </svg>
  <div class="brand" style="left:12px;top:14px;font-size:9px"><span class="brand-dot"></span><span class="brand-name">Hollis Care Partners<span class="brand-tag">a KOFP clinic</span></span></div>
  <div class="contact on-blue" style="left:195px;top:320px">2846 Orwen Ln, Suite B<br>Lindale, TX 75829</div>
</div>
<div class="caption" style="left:372px;top:687px;width:264px">Letterhead Option 2</div>

<!-- Presentation folder -->
<div class="piece" style="left:684px;top:336px;width:468px;height:360px;background:transparent;box-shadow:none;overflow:visible">
  <svg class="wave" viewBox="0 0 468 360" style="filter:drop-shadow(0 2px 4px rgba(0,0,0,.35))">
    <path d="M0 0 H468 V360 H310 V335 H180 V360 H0Z" fill="var(--paper)"/>
    <path d="M0 130 C120 90 260 200 468 110 V360 H310 V335 H180 V360 H0Z" fill="var(--brand-blue)"/>
    <path d="M0 130 C120 90 260 200 468 110" fill="none" stroke="var(--rule-grey)" stroke-width="3"/>
    <path d="M0 205 C150 190 300 230 468 200" fill="none" stroke="var(--brand-blue-dark)" stroke-width="2"/>
    <rect x="105" y="270" width="70" height="40" fill="var(--paper)"/>
    <path d="M105 296 C125 290 150 304 175 292 V310 H105Z" fill="var(--brand-blue)"/>
    <path d="M100 285 L125 275 L150 285" fill="none" stroke="var(--brand-blue-dark)" stroke-width="1"/>
  </svg>
  <div class="brand" style="left:330px;top:28px;font-size:10px"><span class="brand-dot"></span><span class="brand-name">Hollis Care Partners<span class="brand-tag">a KOFP clinic</span></span></div>
  <div class="contact on-blue" style="left:390px;top:226px">2846 Orwen Ln, Suite B<br>Lindale, TX 75829</div>
</div>
<div class="caption" style="left:684px;top:699px;width:468px">Presentation Folder</div>

</body>
</html>
```